Label and packaging design for a cosmetic oil brand

I would like you to design the label and inside (bottle) / outside (box) packaging of my cosmetic Argan Oil brand.

I hope you can design a high quality label and packaging that stands out from the competition, highlighting sustainability and the elegance of a cosmetic brand.

You will find in the Word document attached more details on the specifications and the text for the label. Also, you will find examples of packaging styles that I like.

Thank you.

```html
<!DOCTYPE html>
<html lang="en">
<head>
<meta charset="utf-8">
<title>Argan Oil Label</title>
<link href="https://fonts.googleapis.com/css2?family=Montserrat:wght@300;400&family=Great+Vibes&display=swap" rel="stylesheet">
<style>
  :root {
    --page: #f3f2f0;
    --label: #ffffff;
    --ink: #2b2727;
    --taupe: #8a7f77;
    --floral: #e6ddd3;
    --floral-soft: #f4efe9;
    --rule: #b9b2ac;
  }
  * { margin: 0; padding: 0; box-sizing: border-box; }
  html, body {
    width: 1200px; height: 1070px; overflow: hidden;
    background: var(--page);
  }
  .canvas {
    position: relative; width: 1200px; height: 1070px;
  }
  .label {
    position: absolute; left: 280px; top: 85px;
    width: 640px; height: 900px;
    background: var(--label);
    border: 1px solid #e4e1dd;
    font-family: "Montserrat", sans-serif;
    color: var(--ink);
    overflow: hidden;
  }
  .floral-top, .floral-bottom {
    position: absolute; left: 0; width: 100%;
  }
  .floral-top {
    top: 0; height: 200px;
    background: linear-gradient(180deg, var(--floral) 0%, var(--floral-soft) 55%, rgba(255,255,255,0) 100%);
  }
  .floral-bottom {
    bottom: 0; height: 200px;
    background: linear-gradient(0deg, var(--floral) 0%, var(--floral-soft) 55%, rgba(255,255,255,0) 100%);
  }
  .brand {
    position: absolute; top: 200px; left: 0; width: 100%;
    text-align: center;
  }
  .brand-mark {
    display: inline-block; width: 18px; height: 18px;
    border-radius: 50%; background: var(--taupe);
  }
  .brand-name {
    display: block; margin-top: 6px;
    font-size: 11px; font-weight: 400; letter-spacing: 2px;
    color: var(--taupe);
  }
  .brand-tagline {
    display: block; margin-top: 2px;
    font-size: 7px; font-weight: 300; letter-spacing: 0.5px;
    color: var(--taupe);
  }
  .title {
    position: absolute; top: 275px; left: 0; width: 100%;
    display: flex; justify-content: center;
    font-size: 42px; font-weight: 300; line-height: 52px;
  }
  .title-en { text-align: right; padding-right: 16px; }
  .title-fr { text-align: left; padding-left: 16px; }
  .title-divider { width: 1px; background: var(--rule); }
  .ornament {
    position: absolute; top: 500px; left: 308px;
    width: 24px; height: 28px;
    background: radial-gradient(circle, var(--taupe) 0%, var(--floral) 70%, rgba(255,255,255,0) 100%);
    border-radius: 50%;
  }
  .tagline {
    position: absolute; top: 552px; left: 0; width: 100%;
    text-align: center;
    font-family: "Great Vibes", cursive;
    font-size: 26px; line-height: 36px;
  }
  .rule {
    position: absolute; top: 650px; left: 200px;
    width: 240px; height: 1px; background: var(--rule);
  }
  .volume {
    position: absolute; top: 672px; left: 0; width: 100%;
    text-align: center; font-size: 22px; font-weight: 300;
  }
</style>
</head>
<body>
<div class="canvas">
  <div class="label">
    <div class="floral-top" role="img" aria-label="Fine line drawing of roses, leaves and wildflowers in soft beige"></div>
    <div class="floral-bottom" role="img" aria-label="Fine line drawing of wildflowers and stems in soft beige"></div>

    <div class="brand">
      <span class="brand-mark"></span>
      <span class="brand-name">SOLENARA</span>
      <span class="brand-tagline">pure oils from the argan grove</span>
    </div>

    <div class="title">
      <div class="title-en">100% Pure<br>Cosmetic<br>Argan Oil<br>of Morocco</div>
      <div class="title-divider"></div>
      <div class="title-fr">Huile d’Argan<br>cosmétique<br>du Maroc<br>100% pure</div>
    </div>

    <div class="ornament" role="img" aria-label="Small dandelion flower ornament"></div>

    <p class="tagline">Natural Hair and Skin Care<br>Soins naturels de la peau et des cheveux</p>

    <div class="rule"></div>
    <p class="volume">1 oz | 30 ml</p>
  </div>
</div>
</body>
</html>
```